BriarLoom Website Homepage Design

Please provide your idea of homepage for a hosting company. This project is for DESIGN only, no coding.

It must use/combine colors used in logo, clean, modern look.

Homepage must consist of at least 4 sections (example: testimonials, services, and so on. not necesarily all of them). We would like the navigation to be horizontal, but not mandatory.

You can include a preview of services page (optional, not a must).

Number of Pages Required

1 page

Font styles to use
Sans Serif

```html
<!DOCTYPE html>
<html lang="en">
<head>
<meta charset="utf-8">
<title>BriarLoom – Fast and secure web hosting</title>
<link rel="stylesheet" href="https://fonts.googleapis.com/css2?family=Poppins:wght@300;400;500;600;700&display=swap">
<style>
:root{
  --blue:#1565d8;
  --ink:#1f2a44;
  --text:#6b7488;
  --band:#f3f5f9;
  --white:#ffffff;
  --star:#f5b400;
  --line:#e3e7ef;
  --icon-ring:#d5dbe6;
}
*{margin:0;padding:0;box-sizing:border-box}
html,body{width:1200px;height:2684px;overflow:hidden;background:var(--white)}
body{font-family:"Poppins",sans-serif;color:var(--ink);position:relative}
.btn{display:inline-block;background:var(--blue);color:var(--white);font-size:13px;font-weight:600;letter-spacing:.5px;padding:10px 24px;border-radius:22px;text-decoration:none}
.eyebrow{color:var(--blue);font-weight:500}
.headline{font-weight:400;color:var(--ink)}
p{color:var(--text)}

/* header */
.site-header{position:absolute;top:28px;left:40px;right:40px;height:44px;display:flex;align-items:center;justify-content:space-between}
.brand{display:flex;align-items:center;gap:10px;font-weight:700;font-size:28px;color:var(--blue);letter-spacing:1px}
.brand-square{width:16px;height:16px;background:var(--blue);border-radius:3px}
.main-nav{display:flex;align-items:center;gap:34px;font-size:14px;color:var(--ink)}
.main-nav .sign-in{border:2px solid var(--blue);color:var(--blue);font-weight:600;padding:5px 16px;border-radius:16px;font-size:13px}

/* hero */
.hero{position:absolute;top:220px;left:96px;width:470px}
.hero .eyebrow{font-size:22px}
.hero .headline{font-size:48px;line-height:54px;margin-top:4px}
.hero p{font-size:15px;line-height:24px;margin:16px 0 24px;max-width:420px}
.hero-art{position:absolute;top:80px;left:580px;width:540px;height:360px;border-radius:180px 180px 40px 40px;background:radial-gradient(ellipse at 50% 40%,#cfe0fb 0%,#e8f0fd 55%,#ffffff 100%)}

/* about */
.about-art{position:absolute;top:690px;left:0;width:480px;height:310px;background:linear-gradient(135deg,#eef3fb,#dde7f7);border-radius:0 14px 14px 0}
.about{position:absolute;top:668px;left:600px;width:500px}
.about .eyebrow{font-size:22px}
.about .headline{font-size:38px;line-height:46px;margin-top:2px}
.about p{font-size:14px;line-height:24px;margin:14px 0 20px}
.read-more{font-size:13px;font-weight:600;color:var(--ink);letter-spacing:.5px;padding-bottom:4px;border-bottom:2px solid var(--blue);text-decoration:none}

/* services */
.services-band{position:absolute;top:1060px;left:0;width:1200px;height:680px}
.section-title{position:absolute;left:0;width:1200px;text-align:center}
.section-title .eyebrow{display:block;font-size:26px;line-height:34px}
.section-title .headline{font-size:44px;line-height:52px}
.services-title{top:1200px}
.service-list{position:absolute;top:1330px;left:120px;width:960px;display:flex;justify-content:space-between}
.service{width:230px;text-align:center}
.service-icon{width:120px;height:120px;display:block;margin:0 auto}
.service h3{font-size:22px;font-weight:500;color:var(--ink);margin-top:18px;white-space:nowrap}
.service p{font-size:14px;line-height:23px;margin-top:8px;padding:0 10px}

/* reviews */
.reviews-title{top:1745px}
.review-track{position:absolute;top:1880px;left:0;width:1200px;height:240px}
.review{position:absolute;top:0;width:330px;height:226px;background:var(--white);border-radius:10px;box-shadow:0 8px 28px rgba(31,42,68,.12);padding:26px 28px}
.review p{font-size:14px;line-height:22px}
.reviewer{display:flex;align-items:center;gap:12px;margin-top:18px}
.avatar{width:44px;height:44px;border-radius:50%;background:linear-gradient(135deg,#c9a98e,#8c6f5b)}
.stars{color:var(--star);font-size:14px;letter-spacing:2px;line-height:18px}
.reviewer-name{font-size:13px;color:var(--text)}
.dots{position:absolute;top:2144px;left:0;width:1200px;display:flex;justify-content:center;gap:8px}
.dots span{width:9px;height:9px;border-radius:50%;background:#c9d3e4}
.dots span.active{background:var(--blue)}
.divider{position:absolute;top:2214px;left:96px;width:1008px;height:1px;background:var(--line)}

/* cta */
.cta{position:absolute;top:2280px;left:0;width:1200px;text-align:center}
.cta h2{font-size:44px;font-weight:400;color:var(--ink);line-height:54px}
.cta p{font-size:16px;margin:4px 0 20px}

/* footer */
.site-footer{position:absolute;top:2440px;left:0;width:1200px;height:244px}
.footer-wave{position:absolute;top:0;left:0}
.footer-inner{position:absolute;top:110px;left:96px;right:96px;display:flex;justify-content:space-between;align-items:center}
.footer-brand{font-weight:700;font-size:32px;color:var(--white);letter-spacing:1px}
.footer-nav{display:flex;gap:32px;font-size:15px;font-weight:500;color:var(--white)}
.footer-bottom{position:absolute;top:198px;left:96px;right:96px;display:flex;justify-content:space-between;align-items:center;border-top:1px solid rgba(255,255,255,.25);padding-top:12px}
.copyright{font-size:13px;color:var(--white)}
.social{display:flex;gap:10px}
.social span{width:24px;height:24px;border-radius:50%;background:rgba(255,255,255,.3)}
</style>
</head>
<body>

<header class="site-header">
  <div class="brand"><span class="brand-square"></span>BRIARLOOM</div>
  <nav class="main-nav">
    <span>Hosting</span><span>PRO Hosting</span><span>Domains</span><span>Support</span><span>Affiliates</span>
    <span class="sign-in">SIGN IN</span>
  </nav>
</header>

<section class="hero">
  <div class="eyebrow">BriarLoom Hosting</div>
  <h1 class="headline">Fast and secure<br>web hosting</h1>
  <p>Unlimited storage, unmetered bandwidth, unbeatable hosting. This game's got ye covered.</p>
  <a class="btn" href="#">GET STARTED</a>
</section>
<div class="hero-art" role="img" aria-label="Illustration of blue clouds surrounding stacked server racks"></div>

<div class="about-art" role="img" aria-label="Illustration of a hosting dashboard window with a feature menu: data protection, online security, server, cloud hosting"></div>
<section class="about">
  <div class="eyebrow">About Us</div>
  <h2 class="headline">Level up your web hosting with these must-haves.</h2>
  <p>Lorem Ipsum is simply dummy text of the printing and typesetting industry. Lorem Ipsum has been the industry's standard dummy text ever since the 1500s, when an unknown printer took a galley of type and scrambled it to make a type specimen book.</p>
  <a class="read-more" href="#">READ MORE</a>
</section>

<svg class="services-band" viewBox="0 0 1200 680" aria-hidden="true">
  <path d="M0 140 Q600 -40 1200 140 L1200 560 Q600 720 0 560 Z" fill="#f3f5f9"/>
</svg>
<div class="section-title services-title">
  <span class="eyebrow">Our Services</span>
  <h2 class="headline">What we offer</h2>
</div>
<div class="service-list">
  <div class="service">
    <svg class="service-icon" viewBox="0 0 130 130"><circle cx="65" cy="65" r="60" fill="#fff" stroke="#d5dbe6" stroke-width="2"/><rect x="38" y="44" width="54" height="38" rx="4" fill="none" stroke="#1f2a44" stroke-width="3"/><line x1="38" y1="54" x2="92" y2="54" stroke="#1f2a44" stroke-width="3"/><line x1="55" y1="92" x2="75" y2="92" stroke="#1f2a44" stroke-width="3"/></svg>
    <h3>Web Hosting</h3>
    <p>Lorem Ipsum is simply dummy text of the printing and typesetting industry lorem.</p>
  </div>
  <div class="service">
    <svg class="service-icon" viewBox="0 0 130 130"><circle cx="65" cy="65" r="60" fill="#1565d8"/><path d="M54 50 L40 65 L54 80" fill="none" stroke="#fff" stroke-width="4" stroke-linecap="round" stroke-linejoin="round"/><path d="M76 50 L90 65 L76 80" fill="none" stroke="#fff" stroke-width="4" stroke-linecap="round" stroke-linejoin="round"/><line x1="70" y1="46" x2="60" y2="84" stroke="#fff" stroke-width="4" stroke-linecap="round"/></svg>
    <h3>SitePress Hosting</h3>
    <p>Lorem Ipsum is simply dummy text of the printing and typesetting industry lorem.</p>
  </div>
  <div class="service">
    <svg class="service-icon" viewBox="0 0 130 130"><circle cx="65" cy="65" r="60" fill="#fff" stroke="#d5dbe6" stroke-width="2"/><path d="M40 48 H48 L56 78 H86 L92 56 H52" fill="none" stroke="#1f2a44" stroke-width="3" stroke-linejoin="round"/><circle cx="60" cy="88" r="4" fill="#1f2a44"/><circle cx="82" cy="88" r="4" fill="#1f2a44"/></svg>
    <h3>ShopCart Hosting</h3>
    <p>Lorem Ipsum is simply dummy text of the printing and typesetting industry lorem.</p>
  </div>
  <div class="service">
    <svg class="service-icon" viewBox="0 0 130 130"><circle cx="65" cy="65" r="60" fill="#fff" stroke="#d5dbe6" stroke-width="2"/><path d="M46 82 A14 14 0 0 1 48 54 A18 18 0 0 1 82 52 A15 15 0 0 1 84 82 Z" fill="none" stroke="#1f2a44" stroke-width="3" stroke-linejoin="round"/></svg>
    <h3>Cloud Hosting</h3>
    <p>Lorem Ipsum is simply dummy text of the printing and typesetting industry lorem.</p>
  </div>
</div>

<div class="section-title reviews-title">
  <span class="eyebrow">Testimonials</span>
  <h2 class="headline">Reviews</h2>
</div>
<div class="review-track">
  <div class="review" style="left:-260px"><p>Lorem ipsum dolor sit amet, consectetur adipiscing elit. Cras vel lorem sit amet urna pretium pellentesque sed a neque.</p></div>
  <div class="review" style="left:96px">
    <p>Lorem ipsum dolor sit amet, consectetur adipiscing elit. Cras vel lorem sit amet urna pretium pellentesque sed a neque. Aenean sit amet nisi quam. Vivamus tellus ligula eleifend.</p>
    <div class="reviewer"><span class="avatar" role="img" aria-label="Customer portrait"></span><div><div class="stars">★★★★★</div><div class="reviewer-name">— Marlo (Perth)</div></div></div>
  </div>
  <div class="review" style="left:444px">
    <p>Lorem ipsum dolor sit amet, consectetur adipiscing elit. Cras vel lorem sit amet urna pretium pellentesque sed a neque. Aenean sit amet nisi quam. Vivamus tellus ligula eleifend.</p>
    <div class="reviewer"><span class="avatar" role="img" aria-label="Customer portrait"></span><div><div class="stars">★★★★★</div><div class="reviewer-name">— Greta (Dundee)</div></div></div>
  </div>
  <div class="review" style="left:792px">
    <p>Lorem ipsum dolor sit amet, consectetur adipiscing elit. Cras vel lorem sit amet urna pretium pellentesque sed a neque. Aenean sit amet nisi quam. Vivamus tellus ligula eleifend.</p>
    <div class="reviewer"><span class="avatar" role="img" aria-label="Customer portrait"></span><div><div class="stars">★★★★★</div><div class="reviewer-name">— Ilan (Oslo)</div></div></div>
  </div>
  <div class="review" style="left:1150px"><p>Lorem ipsum dolor sit amet, consectetur adipiscing elit.</p></div>
</div>
<div class="dots"><span class="active"></span><span></span><span></span></div>
<div class="divider"></div>

<section class="cta">
  <h2>Try BriarLoom today</h2>
  <p>Integrating it into your app is easy.</p>
  <a class="btn" href="#">GET STARTED</a>
</section>

<footer class="site-footer">
  <svg class="footer-wave" width="1200" height="244" viewBox="0 0 1200 244" aria-hidden="true">
    <path d="M0 60 Q600 -20 1200 60 L1200 244 L0 244 Z" fill="#1565d8"/>
  </svg>
  <div class="footer-inner">
    <div class="footer-brand">BRIARLOOM</div>
    <nav class="footer-nav"><span>About Us</span><span>Cookie Policy</span><span>Terms of Use</span><span>Privacy Policy</span><span>Sitemap</span><span>Partner With Us</span></nav>
  </div>
  <div class="footer-bottom">
    <span class="copyright">©Copyright 2021 | All Rights Reserved</span>
    <div class="social"><span></span><span></span><span></span><span></span><span></span></div>
  </div>
</footer>

</body>
</html>
```